PRP Poster

We need a poster for a doctors room to encourage people to enquire about PRP procedure.

It needs to include "for osteoarthritis and sports injuries" and "enhancing the body's natural ability to heal".

A brochure is attached which outlines what PRP (Platelet Rich Plasma) is, in the brochure it is called NTQ. DO NOT USE ANY OF THE LOGOS FROM THIS BROCHURE.

Target Market(s)

patients in an orthopaedic surgery waiting room/area
age range from teenagers till 80year olds
male= female ratio

Requirements
Must have
• single poster
eye-catching yet professional
needs to be suitable/appropriate for the waiting area of a surgeons clinic
Nice to have
• prp is a natural therapy (it is essentially the person's own blood being reinjected to a site of injury)
the "natural" aspect of the therapy needs to be emphasised

```html
<!DOCTYPE html>
<html lang="en">
<head>
<meta charset="utf-8">
<title>PRP – Platelet Rich Plasma</title>
<link rel="stylesheet" href="https://fonts.googleapis.com/css2?family=Oswald:wght@300;400;500;600;700&display=swap">
<style>
  :root {
    --blood-deep: #5a0a0a;
    --blood-mid: #a8160f;
    --blood-bright: #e0261b;
    --sky-blue: #1a76bc;
    --navy: #1c3460;
    --white: #ffffff;
    --ink: #111111;
    --accent-red: #e8232a;
    --text-blue: #1a76bc;
  }
  * { margin: 0; padding: 0; box-sizing: border-box; }
  html, body { width: 848px; height: 1200px; overflow: hidden; background: var(--white); }
  .poster {
    position: relative; width: 848px; height: 1200px; overflow: hidden;
    font-family: "Oswald", "Arial Narrow", sans-serif;
    background: var(--sky-blue);
  }
  .cells-backdrop {
    position: absolute; left: 0; top: 0; width: 848px; height: 268px;
    background:
      radial-gradient(circle at 20% 30%, var(--blood-bright) 0, transparent 22%),
      radial-gradient(circle at 55% 15%, #ff3a2a 0, transparent 18%),
      radial-gradient(circle at 80% 45%, var(--blood-bright) 0, transparent 20%),
      radial-gradient(circle at 40% 70%, #c81c12 0, transparent 20%),
      linear-gradient(180deg, var(--blood-mid), #6e0f0b 70%, #8a2a1a);
  }
  .monogram { position: absolute; left: 0; top: 0; width: 848px; height: 600px; }
  .title {
    position: absolute; left: 0; top: 560px; width: 848px;
    text-align: center; color: var(--white);
    font-weight: 600; font-size: 96px; line-height: 1; letter-spacing: -1px;
  }
  .tagline-band {
    position: absolute; left: 0; top: 668px; width: 848px; height: 154px;
    background: var(--white); text-align: center;
  }
  .tagline {
    margin-top: 12px; font-weight: 300; font-size: 52px; line-height: 1.2;
    color: var(--text-blue);
  }
  .tagline .emphasis { color: var(--accent-red); font-weight: 700; }
  .tagline .lead { font-weight: 400; }
  .explainer {
    margin-top: 6px; font-weight: 500; font-size: 22px; color: var(--ink);
  }
  .lower-panel {
    position: absolute; left: 0; top: 822px; width: 848px; height: 378px;
    background: var(--navy);
  }
  .anatomy-collage {
    position: absolute; left: 180px; top: 8px; width: 445px; height: 360px;
    background: radial-gradient(ellipse at 50% 45%, #4a7fc0 0, #27508a 45%, var(--navy) 80%);
  }
  .conditions-badge {
    position: absolute; left: 17px; top: 92px; width: 178px; height: 178px;
    border-radius: 50%; background: var(--accent-red);
    display: flex; align-items: center; justify-content: center;
    color: var(--white); text-align: center;
    font-weight: 500; font-size: 30px; line-height: 1.05;
  }
  .conditions-badge span { transform: rotate(-22deg); display: block; }
  .healing-message {
    position: absolute; left: 628px; top: 28px; width: 210px;
    text-align: center; color: var(--white);
    font-weight: 400; font-size: 50px; line-height: 1.06;
  }
  .healing-message .emphasis { color: var(--accent-red); font-weight: 600; font-size: 60px; }
</style>
</head>
<body>
<main class="poster">
  <div class="cells-backdrop" role="img" aria-label="Close-up illustration of red blood cells"></div>

  <svg class="monogram" viewBox="0 0 848 600" aria-label="PRP">
    <defs>
      <radialGradient id="cellFill" cx="50%" cy="40%" r="70%">
        <stop offset="0" stop-color="#d3241a"/>
        <stop offset="0.5" stop-color="#a3150f"/>
        <stop offset="1" stop-color="#5a0a0a"/>
      </radialGradient>
    </defs>
    <text x="424" y="566" text-anchor="middle" textLength="770" lengthAdjust="spacingAndGlyphs"
          font-family="Oswald, sans-serif" font-weight="700" font-size="600"
          fill="url(#cellFill)" stroke="#3a0606" stroke-opacity="0.35" stroke-width="3">PRP</text>
  </svg>

  <h1 class="title">Platelet Rich Plasma</h1>

  <section class="tagline-band">
    <p class="tagline"><span class="lead">A new method of</span> <span class="emphasis">NATURAL</span> therapy</p>
    <p class="explainer">It is essentially the person's own blood being reinjected to a site of injury</p>
  </section>

  <section class="lower-panel">
    <div class="anatomy-collage" role="img" aria-label="Collage of glowing X-ray style anatomy panels showing knee, spine, hand, foot, hip and shoulder joints"></div>
    <div class="conditions-badge"><span>osteoarthritis<br>and sports<br>injuries</span></div>
    <p class="healing-message">enhancing the body's <span class="emphasis">natural</span><br>ability<br>to heal</p>
  </section>
</main>
</body>
</html>
```